Brava Set CEO and Partners Business Card

We need a fresh, fun, simple and clean business card design....we would like a template where we can add a name and title (as well as specific email addresses). We are open to different looks (full logo on one side and a small logo on the company info side, or our logo is in the background but faint on one side but full on the other, or something else cool :-) ). Our colors are in our logo: blue, black and white...however we are not opposed to the use of other colors if it works. We build sets, make props and a host of other things for the film and television industry...our card should reflect creativity, style and professionalism.

A white background would be preferred.

I would like to see an option with Facebook and Instagram icons.

Facebook- facebook.com/bravasetny
Instagram- brava_set

Our website is bravaset-example.com.

Brava Set, Inc.
418 Corvell Avenue, Unit 9
North Hollywood, California 91602
555.210.4873 | tel
555.210.6692 | fax
www.BravaSet-example.com

Sample Name and Title #1:

Peter Halvik
CEO / Co-Owner
555.210.4873 | tel
555.210.6692 | fax
peter@bravaset-example.com
www.BravaSet-example.com

Target Market(s)

Marketing Professionals, Production Designers, Interior Designers, Film Producers, Directors, Art Directors, Event Directors

Industry/Entity Type

Entertainment Industry

Contact Information for Business Card

Peter Halvik
CEO / Co-Owner
555.210.4873 | tel
555.210.6692 | fax
peter@bravaset-example.com
www.BravaSet-example.com

Font styles to use
Sans Serif

Colors
33a6d7
ffffff
1b1b1b

Requirements
Must have
• Logo, All Contact Info, White Background. Symmetry.
Nice to have
• Facebook and Instagram icons with addresses
• Facebook- facebook.com/bravasetny
• Instagram- brava_set

```html
<!DOCTYPE html>
<html lang="en">
<head>
<meta charset="utf-8">
<title>Brava Set Business Card</title>
<link rel="stylesheet" href="https://fonts.googleapis.com/css2?family=Open+Sans:wght@400;600;800&display=swap">
<style>
  :root {
    --brand-blue: #33a6d7;
    --brand-black: #1b1b1b;
    --brand-white: #ffffff;
    --card-dark: #0b0b0b;
    --muted-grey: #bdbdbd;
    --backdrop: #e4e5e7;
  }
  * { box-sizing: border-box; margin: 0; padding: 0; }
  html, body {
    width: 1200px; height: 800px; overflow: hidden;
    background: var(--backdrop);
    font-family: "Open Sans", Arial, sans-serif;
  }
  .stage {
    position: relative; width: 1200px; height: 800px;
  }
  .card {
    position: absolute; top: 251px;
    width: 520px; height: 298px;
    border-radius: 3px;
    box-shadow: 0 6px 18px rgba(0,0,0,.12);
    overflow: hidden;
  }
  .card--info { left: 50px; background: var(--card-dark); color: var(--brand-white); }
  .card--logo { left: 630px; background: var(--brand-white); }

  /* Info side */
  .holder { position: absolute; left: 26px; top: 22px; }
  .holder__name { color: var(--brand-blue); font-size: 21px; font-weight: 600; line-height: 1.1; }
  .holder__title { color: var(--muted-grey); font-size: 11px; margin-top: 2px; }

  .card__art--faint {
    position: absolute; left: 40px; top: 70px; width: 230px; height: 170px;
    border-radius: 6px;
    background: linear-gradient(120deg, rgba(120,140,60,.18), rgba(150,60,90,.18));
  }

  .contact {
    position: absolute; right: 26px; top: 98px;
    text-align: right; font-size: 12.5px; line-height: 1.5;
  }
  .contact__label { color: var(--brand-blue); }
  .contact__address { margin-top: 2px; }

  .wordmark { font-weight: 800; letter-spacing: -0.5px; line-height: 1; }
  .card--info .wordmark {
    position: absolute; left: 210px; top: 218px;
    font-size: 38px; color: var(--brand-white);
  }

  .social {
    position: absolute; right: 26px; bottom: 16px;
    display: flex; gap: 16px; font-size: 12px;
  }
  .social__item { display: flex; align-items: center; gap: 5px; }
  .social__mark { width: 11px; height: 11px; border-radius: 2px; background: var(--brand-blue); }

  /* Logo side */
  .card__art--pastel {
    position: absolute; left: 20px; top: 20px; width: 300px; height: 190px;
    border-radius: 8px;
    background: linear-gradient(120deg, rgba(240,210,120,.35), rgba(230,160,200,.35), rgba(190,170,230,.35));
  }
  .card--logo .wordmark {
    position: absolute; right: 34px; bottom: 46px;
    font-size: 58px; color: var(--brand-black);
  }
</style>
</head>
<body>
<main class="stage">
  <section class="card card--info" aria-label="Business card, contact side">
    <div class="card__art--faint" role="img" aria-label="Faint line drawing of a vintage camera"></div>
    <header class="holder">
      <h1 class="holder__name">Peter Halvik</h1>
      <p class="holder__title">CEO / Co-Owner</p>
    </header>
    <address class="contact" style="font-style:normal">
      <div><span class="contact__label">T:</span> 555.210.4873</div>
      <div><span class="contact__label">F:</span> 555.210.6692</div>
      <div><span class="contact__label">W:</span> www.BravaSet-example.com</div>
      <div><span class="contact__label">E:</span> peter@bravaset-example.com</div>
      <div class="contact__address">418 Corvell Avenue<br>Unit 9, North Hollywood<br>California 91602</div>
    </address>
    <div class="wordmark">Brava Set</div>
    <div class="social">
      <span class="social__item"><span class="social__mark"></span>bravasetny</span>
      <span class="social__item"><span class="social__mark"></span>brava_set</span>
    </div>
  </section>

  <section class="card card--logo" aria-label="Business card, logo side">
    <div class="card__art--pastel" role="img" aria-label="Pastel rainbow line drawing of a vintage camera"></div>
    <div class="wordmark">Brava Set</div>
  </section>
</main>
</body>
</html>
```